Painting services company needs a DL brochure about their services

We need a brochure describing our painting services including our logo and photos of work. The final design needs to be colourful, vibrant, and targeted to schools, aged care, commercial property maintenance clients.

```html
<!DOCTYPE html>
<html lang="en">
<head>
<meta charset="utf-8">
<title>Brightcoat Painters – DL Brochure</title>
<link rel="stylesheet" href="https://fonts.googleapis.com/css2?family=Oswald:wght@500;700&family=Open+Sans:ital,wght@0,400;0,600;0,700;1,700&display=swap">
<style>
  :root{
    --blue:#2a4a9f;
    --blue-deep:#1f3a85;
    --yellow:#f5d92f;
    --white:#ffffff;
    --paper:#f7f7f8;
    --stage:#e6e7e9;
    --ink:#1d2b5c;
    --photo-a:#8a8f96;
    --photo-b:#c9ccd1;
  }
  *{box-sizing:border-box;margin:0;padding:0}
  html,body{width:1200px;height:2400px;overflow:hidden}
  body{background:var(--stage);font-family:"Open Sans",Arial,sans-serif;position:relative}

  .spread{position:absolute;left:30px;width:1140px;height:808px;display:flex;box-shadow:0 10px 30px rgba(0,0,0,.15);background:var(--white)}
  .spread--outside{top:250px}
  .spread--inside{top:1342px}
  .panel{position:relative;width:380px;height:808px;overflow:hidden}
  .panel + .panel{border-left:1px solid rgba(0,0,0,.06)}
  .panel--blue{background:var(--blue)}
  .panel--white{background:var(--white)}
  .deco{position:absolute;inset:0;width:100%;height:100%}

  .photo{position:absolute;border-radius:50%;background:radial-gradient(circle at 35% 35%,var(--photo-b),var(--photo-a));border:6px solid var(--white)}
  .photo--warm{background:radial-gradient(circle at 40% 40%,#e0c9a8,#8c6b4e)}
  .photo--hall{background:radial-gradient(circle at 50% 40%,#efe9dc,#9b8f7a)}
  .photo--floor{background:radial-gradient(circle at 50% 50%,#7fd0b4,#2e6f6a)}
  .photo--sky{background:radial-gradient(circle at 50% 30%,#c8dcf0,#5f7ea6)}

  .display{font-family:"Oswald",Arial,sans-serif;font-weight:700;text-transform:uppercase;line-height:1.05}

  /* brand lockup */
  .brand{position:absolute;display:flex;align-items:center;gap:10px;background:var(--blue);padding:12px 14px}
  .brand__mark{width:26px;height:26px;background:var(--yellow);flex:none}
  .brand__name{font-family:"Oswald",Arial,sans-serif;font-weight:700;color:var(--white);font-size:20px;line-height:1;text-transform:lowercase;width:96px}

  /* outside: flap */
  .flap__headline{position:absolute;left:34px;top:360px;width:310px;color:var(--blue);font-size:25px}
  .flap__band{position:absolute;left:0;top:520px;width:320px;background:var(--yellow);color:var(--blue);font-weight:700;font-size:11.5px;padding:8px 14px 8px 34px;text-transform:uppercase}
  .flap__copy{position:absolute;left:34px;top:580px;width:300px;font-size:12px;line-height:1.55;color:var(--ink)}

  /* outside: back */
  .back__intro{position:absolute;left:168px;top:52px;width:192px}
  .back__title{color:var(--yellow);font-size:18px;margin-bottom:8px}
  .back__copy{color:var(--white);font-size:11.5px;line-height:1.5}
  .back__cta{position:absolute;left:0;width:100%;top:330px;text-align:center;color:var(--white);font-weight:700;font-style:italic;font-size:21px;line-height:1.2}
  .back__cta em{color:var(--yellow);font-style:italic}
  .back__phone{position:absolute;left:80px;top:400px;width:220px;background:var(--yellow);color:var(--blue);display:flex;align-items:center;justify-content:center;gap:10px;font-family:"Oswald",Arial,sans-serif;font-weight:700;font-size:28px;padding:6px 0;border-radius:4px}
  .back__address{position:absolute;left:0;width:100%;top:462px;text-align:center;color:var(--white);font-size:12px}
  .back__brand{left:125px;top:560px;flex-direction:column;align-items:flex-start;background:var(--white);padding:18px;border:4px solid var(--white);outline:3px solid var(--blue)}
  .back__brand .brand__name{color:var(--blue);width:96px}

  /* outside: cover */
  .cover__brand{right:0;top:40px;flex-direction:column;align-items:flex-start;padding:16px 18px}
  .cover__headline{position:absolute;right:36px;top:560px;text-align:right;color:var(--blue)}
  .cover__headline .l1{font-size:30px;display:block}
  .cover__headline .l2{font-size:56px;display:block}
  .cover__headline .l3{font-size:30px;display:block}
  .cover__tagline{position:absolute;right:36px;top:700px;color:var(--blue);font-size:17px;font-weight:600}
  .cover__web{position:absolute;right:36px;top:736px;background:var(--yellow);color:var(--blue);font-weight:700;font-size:12.5px;padding:6px 16px;border-radius:14px}

  /* inside */
  .section-head{position:absolute;top:34px;height:54px;display:flex;align-items:center;font-size:30px;color:var(--white);background:var(--blue)}
  .section-head--left{left:0;width:360px;padding-left:30px;clip-path:polygon(0 0,100% 0,94% 100%,0 100%)}
  .section-head--mid{left:0;width:380px;padding-left:120px;background:transparent;color:var(--white)}
  .label{position:absolute;background:var(--yellow);color:var(--blue);font-weight:700;font-size:12.5px;text-transform:uppercase;line-height:1.25;padding:7px 14px}
  .services{position:absolute;list-style:none}
  .services li{position:relative;padding-left:30px;margin-bottom:14px;font-size:14px;line-height:1.35}
  .services li::before{content:"";position:absolute;left:0;top:1px;width:19px;height:19px;border-radius:50%;background:var(--blue)}
  .services li::after{content:"";position:absolute;left:6px;top:5px;width:5px;height:9px;border:solid var(--white);border-width:0 2.5px 2.5px 0;transform:rotate(45deg)}
  .services--on-white li{color:var(--ink)}
  .services--on-blue li{color:var(--white)}
  .services--on-blue li::before{background:var(--yellow)}
  .services--on-blue li::after{border-color:var(--blue)}
</style>
</head>
<body>

<!-- OUTSIDE SPREAD -->
<section class="spread spread--outside" aria-label="Brochure outside">

  <!-- flap -->
  <article class="panel panel--white flap">
    <svg class="deco" viewBox="0 0 380 808" aria-hidden="true">
      <circle cx="40" cy="20" r="150" fill="var(--yellow)"/>
      <circle cx="190" cy="170" r="150" fill="none" stroke="var(--blue)" stroke-width="10"/>
      <circle cx="190" cy="170" r="170" fill="none" stroke="var(--blue)" stroke-width="6" stroke-dasharray="260 800" stroke-dashoffset="-40"/>
      <circle cx="330" cy="310" r="16" fill="var(--blue)"/>
      <path d="M0 808 L0 760 Q120 730 200 808 Z" fill="var(--blue)"/>
    </svg>
    <div class="photo photo--sky" style="left:60px;top:40px;width:260px;height:260px" role="img" aria-label="Photo of the company van parked at a job site"></div>
    <h2 class="flap__headline display">Remember, when you need painters for a commercial building, we are the painters with the right attitude</h2>
    <p class="flap__band">We are a family run business with over 40 years experience</p>
    <p class="flap__copy">Our team delivers careful, tidy and reliable painting for schools, aged care homes and commercial properties. We plan every job around your site, work safely and leave each space clean, bright and ready to use.</p>
  </article>

  <!-- back -->
  <article class="panel panel--blue back">
    <svg class="deco" viewBox="0 0 380 808" aria-hidden="true">
      <circle cx="-10" cy="110" r="118" fill="var(--white)"/>
      <circle cx="-10" cy="110" r="138" fill="none" stroke="var(--white)" stroke-width="8"/>
      <circle cx="-10" cy="110" r="156" fill="none" stroke="var(--yellow)" stroke-width="6" stroke-dasharray="160 900" stroke-dashoffset="-40"/>
      <circle cx="330" cy="250" r="14" fill="var(--yellow)"/>
      <path d="M380 620 Q300 700 380 808 Z" fill="var(--yellow)"/>
    </svg>
    <div class="back__intro">
      <h3 class="back__title display">Brightcoat Painters</h3>
      <p class="back__copy">We are a specialist commercial painting company offering professional painting, coating and maintenance services to clients across Australia.</p>
    </div>
    <p class="back__cta">Call or email us <em>NOW</em><br>to get a <em>FAST QUOTE!</em></p>
    <div class="back__phone">
      <svg width="22" height="22" viewBox="0 0 24 24" aria-hidden="true"><path fill="var(--blue)" d="M6.6 10.8a15.1 15.1 0 0 0 6.6 6.6l2.2-2.2a1 1 0 0 1 1-.25 11.4 11.4 0 0 0 3.6.57 1 1 0 0 1 1 1V20a1 1 0 0 1-1 1A17 17 0 0 1 3 4a1 1 0 0 1 1-1h3.5a1 1 0 0 1 1 1c0 1.250.2 2.450.57 3.57a1 1 0 0 1-.25 1z"/></svg>
      1300 555 012
    </div>
    <p class="back__address">P.O. Box 100, Sampleton NSW 2000</p>
    <div class="brand back__brand"><span class="brand__mark"></span><span class="brand__name">brightcoat painters</span></div>
  </article>

  <!-- cover -->
  <article class="panel panel--white cover">
    <svg class="deco" viewBox="0 0 380 808" aria-hidden="true">
      <circle cx="300" cy="240" r="190" fill="var(--yellow)"/>
      <circle cx="170" cy="290" r="175" fill="none" stroke="var(--blue)" stroke-width="10"/>
      <circle cx="170" cy="290" r="200" fill="none" stroke="var(--blue)" stroke-width="6" stroke-dasharray="300 900" stroke-dashoffset="-560"/>
      <circle cx="170" cy="290" r="222" fill="none" stroke="var(--blue)" stroke-width="4" stroke-dasharray="220 900" stroke-dashoffset="-600"/>
      <circle cx="70" cy="540" r="22" fill="var(--blue)"/>
      <circle cx="150" cy="560" r="10" fill="var(--yellow)"/>
    </svg>
    <div class="photo" style="left:20px;top:140px;width:300px;height:300px" role="img" aria-label="Black and white photo of industrial pipe coating work"></div>
    <div class="brand cover__brand"><span class="brand__mark"></span><span class="brand__name">brightcoat painters</span></div>
    <h1 class="cover__headline display"><span class="l1">Friendly</span><span class="l2">Painting</span><span class="l3">Contractors</span></h1>
    <p class="cover__tagline">Commercial Painters in Australia</p>
    <p class="cover__web">www.brightcoatpainters.com.au</p>
  </article>
</section>

<!-- INSIDE SPREAD -->
<section class="spread spread--inside" aria-label="Brochure inside">

  <article class="panel panel--white">
    <svg class="deco" viewBox="0 0 380 808" aria-hidden="true">
      <circle cx="40" cy="760" r="140" fill="var(--yellow)"/>
      <circle cx="200" cy="680" r="150" fill="none" stroke="var(--blue)" stroke-width="8"/>
      <circle cx="360" cy="560" r="12" fill="var(--blue)"/>
    </svg>
    <h2 class="section-head section-head--left display">Specialist Painting</h2>
    <p class="label" style="left:30px;top:110px;width:250px">Commercial &amp; Industrial<br>Painting Services</p>
    <ul class="services services--on-white" style="left:30px;top:172px;width:320px">
      <li>Pressure cleaning of building facades</li>
      <li>Painting of broad areas and sites to commercial interiors and exteriors</li>
      <li>Corrosion repairs and protective coatings for steel</li>
      <li>On-site spray painting</li>
      <li>Texture coatings</li>
      <li>After-hours and weekends available</li>
    </ul>
    <div class="photo photo--hall" style="left:90px;top:560px;width:220px;height:220px" role="img" aria-label="Photo of a freshly painted aged care corridor"></div>
  </article>

  <article class="panel panel--blue">
    <svg class="deco" viewBox="0 0 380 808" aria-hidden="true">
      <circle cx="-30" cy="40" r="130" fill="var(--white)"/>
      <circle cx="90" cy="690" r="120" fill="none" stroke="var(--white)" stroke-width="6" stroke-dasharray="6 10"/>
      <circle cx="300" cy="560" r="10" fill="var(--yellow)"/>
    </svg>
    <h2 class="section-head section-head--mid display">Contractors</h2>
    <div class="photo photo--sky" style="left:20px;top:20px;width:110px;height:110px" role="img" aria-label="Photo of a coated rooftop surface"></div>
    <p class="label" style="left:30px;top:158px;width:250px">Floor Preparation and<br>Coating Services</p>
    <ul class="services services--on-blue" style="left:30px;top:220px;width:320px">
      <li>Diamond grinding</li>
      <li>Shot blasting</li>
      <li>Glue and surface removal</li>
      <li>Epoxy and polyurethane coatings</li>
      <li>Anti-slip coatings</li>
      <li>Epoxy floors for warehouse and workshop</li>
    </ul>
    <div class="photo photo--sky" style="left:20px;top:600px;width:150px;height:150px" role="img" aria-label="Photo of a painted warehouse interior"></div>
    <div class="photo photo--warm" style="left:220px;top:610px;width:130px;height:130px" role="img" aria-label="Photo of a finished commercial floor"></div>
  </article>

  <article class="panel panel--white">
    <svg class="deco" viewBox="0 0 380 808" aria-hidden="true">
      <path d="M0 320 Q190 260 380 300 L380 808 L0 808 Z" fill="var(--blue)"/>
      <circle cx="330" cy="40" r="110" fill="var(--yellow)"/>
      <circle cx="200" cy="150" r="150" fill="none" stroke="var(--blue)" stroke-width="8" stroke-dasharray="320 900" stroke-dashoffset="-520"/>
      <circle cx="40" cy="260" r="14" fill="var(--yellow)"/>
    </svg>
    <div class="photo photo--warm" style="left:80px;top:20px;width:260px;height:260px" role="img" aria-label="Photo of a painted commercial reception area"></div>
    <p class="label" style="left:30px;top:350px;width:240px">New Construction<br>Painting Services</p>
    <ul class="services services--on-blue" style="left:30px;top:412px;width:320px">
      <li>Painting of new buildings</li>
      <li>Interiors and exteriors</li>
      <li>Spray painting and texture coatings</li>
    </ul>
    <div class="photo photo--floor" style="left:100px;top:560px;width:200px;height:200px" role="img" aria-label="Photo of a green epoxy coated floor"></div>
  </article>
</section>

</body>
</html>
```